HomeBridle business card and stationary design

We are looking for a simple yet elegant design for our mortgage company business card and stationary.

The card should include:
Name (Derek Walsh)
Title (CEO)
Phone Number (614-208-3917)
Address (48 Birchfield Court, Suite 314, Marlow, OH 43952)
Email (email@homebridle-example.com)
"NMLS" i.e. (NMLS 61947)
"Company NMLS" (Company NMLS 472815)

See above

```html
<!DOCTYPE html>
<html lang="en">
<head>
<meta charset="utf-8">
<title>HomeBridle Business Card</title>
<link rel="stylesheet" href="https://fonts.googleapis.com/css2?family=Arimo:wght@700&family=Tinos:wght@700&display=swap">
<style>
  :root {
    --backdrop: #4a4a4a;
    --card-black: #232323;
    --texture-grey: #2f2f2f;
    --stripe-grey: #3a3a3a;
    --brand-blue: #22a3e0;
    --name-grey: #c9c9c9;
    --text-white: #ffffff;
  }
  * { margin: 0; padding: 0; box-sizing: border-box; }
  html, body {
    width: 1200px;
    height: 988px;
    overflow: hidden;
    background: var(--backdrop);
  }
  .business-card {
    position: absolute;
    left: 174px;
    top: 234px;
    width: 852px;
    height: 518px;
    background: var(--card-black);
    overflow: hidden;
  }
  .card-graphics {
    position: absolute;
    inset: 0;
    width: 852px;
    height: 518px;
  }
  .brand-name {
    position: absolute;
    left: 318px;
    top: 108px;
    font-family: "Arimo", Arial, sans-serif;
    font-weight: 700;
    font-size: 84px;
    line-height: 1;
    color: var(--text-white);
    letter-spacing: -1px;
  }
  .holder {
    position: absolute;
    left: 54px;
    top: 205px;
    font-family: "Tinos", "Times New Roman", serif;
    font-weight: 700;
    color: var(--name-grey);
  }
  .holder-name { font-size: 37px; line-height: 1; }
  .holder-title { font-size: 22px; line-height: 1; margin: 8px 0 0 6px; }
  .contact-list {
    position: absolute;
    left: 403px;
    top: 212px;
    list-style: none;
    font-family: "Arimo", Arial, sans-serif;
    font-weight: 700;
    font-size: 23px;
    color: var(--text-white);
  }
  .contact-item {
    display: flex;
    align-items: flex-start;
    line-height: 37.5px;
  }
  .contact-item .bullet {
    width: 17px;
    height: 15px;
    margin: 12px 13px 0 0;
    flex: none;
  }
  .contact-item .continued { padding-left: 30px; }
</style>
</head>
<body>
  <div class="business-card">
    <svg class="card-graphics" viewBox="0 0 852 518" aria-hidden="false">
      <rect role="img" aria-label="halftone dot texture band" x="0" y="0" width="852" height="48" fill="var(--texture-grey)"/>
      <rect role="img" aria-label="halftone dot texture band" x="0" y="450" width="852" height="68" fill="var(--texture-grey)"/>
      <polygon class="corner-stripe" points="0,276 0,306 336,518 372,518" fill="var(--stripe-grey)"/>
      <polygon class="corner-accent" points="0,306 0,518 336,518" fill="var(--brand-blue)"/>
      <polygon class="corner-stripe" points="664,0 684,0 852,114 852,132" fill="var(--stripe-grey)"/>
      <polygon class="corner-accent" points="684,0 852,0 852,114" fill="var(--brand-blue)"/>
    </svg>

    <div class="brand-name">HomeBridle</div>

    <div class="holder">
      <div class="holder-name">Derek Walsh</div>
      <div class="holder-title">CEO</div>
    </div>

    <ul class="contact-list">
      <li class="contact-item"><svg class="bullet" viewBox="0 0 17 15"><polygon points="8.5,0 17,5 17,15 0,15 0,5" fill="var(--brand-blue)"/></svg>614-208-3917</li>
      <li class="contact-item"><svg class="bullet" viewBox="0 0 17 15"><polygon points="8.5,0 17,5 17,15 0,15 0,5" fill="var(--brand-blue)"/></svg>48 Birchfield Court, Suite 314,</li>
      <li class="contact-item"><span class="continued">Marlow, OH 43952</span></li>
      <li class="contact-item"><svg class="bullet" viewBox="0 0 17 15"><polygon points="8.5,0 17,5 17,15 0,15 0,5" fill="var(--brand-blue)"/></svg>email@homebridle-example.com</li>
      <li class="contact-item"><svg class="bullet" viewBox="0 0 17 15"><polygon points="8.5,0 17,5 17,15 0,15 0,5" fill="var(--brand-blue)"/></svg>NMLS 61947</li>
      <li class="contact-item"><svg class="bullet" viewBox="0 0 17 15"><polygon points="8.5,0 17,5 17,15 0,15 0,5" fill="var(--brand-blue)"/></svg>Company NMLS 472815</li>
    </ul>
  </div>
</body>
</html>
```